Pet and Potrait photography business needs web site design

I need a web design that is for a portrait and pet photography business based in Tasmania, Australia. It is a small, simple concept, photography business that focuses on portraits and pet photography only. I need something that is clean, maybe a white background, fun, and appealing to families. The design must make my images stand out and be the focus. The final design needs to show that it is aimed a families, pet owners, and is all about the clients - albeit the two or four legged kinds.

Business name is: maple lantern photography

I need it to be able to have the following:

- Include space for logo design which is also through SketchPlaza
- Home Page which has a gallery of my images (which you can click an arrow - either forward or back - that showcases my images
- About Page
- Portfolio Page (preferably two a) for portraits, and b) for pet photography
- Pricing page
- secure log in client page
- Contact page
Updates

Reason: Waiting for logo design to be completed to fit in with overall website design.

Target Market(s)

Families
Pet owners
Single couples who have fur babies

Industry/Entity Type

Business

Font styles to use
Serif
Decorative
Script

Colors

Designer to choose colors to be used in the design.

Requirements
Must have
• the website must provide the ability for me to upload and change images regularly.
Nice to have
• Logo design is a secondary project that will need to be worked on as well. I will pay an additional amount for those that are prepared to include this in the project.
Should not have
• No graffiti style writing.
It has to be elegant, and stylish and be aimed at females.
Women are going to be the driver for having portraits done of either their babies, children, or fur babies - i.e. pets.

```html
<!DOCTYPE html>
<html lang="en">
<head>
<meta charset="utf-8">
<title>Contact Us – maple lantern photography</title>
<link href="https://fonts.googleapis.com/css2?family=Gelasio:ital,wght@0,400;0,600;1,400&family=Open+Sans:wght@400;600;700&display=swap" rel="stylesheet">
<style>
:root{
  --lilac:#d4bbd5;
  --lilac-line:#e6d6e7;
  --ink:#2f2f2f;
  --text:#555;
  --muted:#888;
  --band:#f3f3f3;
  --footer:#eeeeea;
  --footer-rule:#dcdcdc;
  --dark:#2e2e2e;
  --white:#fff;
}
*{box-sizing:border-box;margin:0;padding:0}
html,body{width:785px;height:1200px;overflow:hidden;background:var(--white)}
body{position:relative;font-family:"Open Sans",sans-serif;color:var(--text)}
.abs{position:absolute}

.brand{left:97px;top:18px;font-family:"Gelasio",serif;font-size:18px;color:var(--ink);display:flex;align-items:center;gap:6px}
.brand-dot{width:8px;height:8px;border-radius:50%;background:var(--lilac)}
.nav{top:24px;right:105px;display:flex;align-items:center;gap:18px;font-size:8px;letter-spacing:1.6px;color:#555}
.nav a{color:inherit;text-decoration:none}
.nav .current{background:var(--lilac);color:var(--white);padding:6px 7px}

.top-rule{left:71px;top:68px;width:629px;height:3px;background:var(--lilac)}
.crumbs{left:71px;top:71px;width:629px;height:24px;background:var(--band);border-bottom:1px solid #e2e2e2;font-size:7px;padding:6px 24px;color:#555}
.crumbs em{font-family:"Gelasio",serif;font-size:7px;margin-right:3px}

.page-title{left:97px;top:113px;font-family:"Gelasio",serif;font-weight:400;font-size:14px;color:var(--ink)}
.label{font-size:8.5px;letter-spacing:1.6px;color:#666;font-weight:400}
.intro{left:97px;top:184px;width:413px;font-size:8.7px;line-height:14.1px;text-align:justify;color:#555}
.details{left:545px;top:186px;font-family:"Gelasio",serif;font-style:italic;font-weight:400;font-size:7.7px;line-height:12.9px;color:#555}

.query-rule{left:287px;top:334px;width:484px;height:1px;background:#f1f1f1}
.form{left:97px;top:350px;width:577px;height:243px;background:var(--lilac)}
.field{position:absolute;left:52px;width:472px;height:23px;background:var(--white);font-style:italic;font-size:8.5px;color:#777;padding:5px 20px;line-height:13px}
.form-rule{position:absolute;left:0;top:208px;width:577px;height:1px;background:var(--lilac-line)}
.submit{position:absolute;left:225px;top:213px;width:125px;height:18px;background:var(--white);border:1px solid #ccc;font-family:"Gelasio",serif;font-style:italic;font-size:11px;color:var(--ink);text-align:center;line-height:16px}

.map{left:97px;top:682px;width:580px;height:178px;background:linear-gradient(90deg,#ecebe6 0%,#dfe9cf 35%,#ecebe6 60%,#d7e6c3 78%,#a9c8f5 100%)}

.footer-rule{left:71px;top:939px;width:629px;height:3px;background:var(--footer-rule)}
.footer{left:71px;top:946px;width:629px;height:196px;background:var(--footer)}
.col{position:absolute;top:22px;width:128px}
.col h4{font-size:7px;letter-spacing:.8px;font-weight:700;color:#333;margin-bottom:7px}
.col p{font-family:"Gelasio",serif;font-style:italic;font-weight:400;font-size:8px;line-height:12.9px;color:var(--muted)}
.col .gap{margin-top:13px}
.col .dark{color:#555}
.more{position:absolute;top:149px;font-size:7.5px;color:#333}
.touch{position:absolute;left:473px;top:138px;width:120px;height:18px;background:var(--dark);color:var(--white);font-family:"Gelasio",serif;font-style:italic;font-size:11px;text-align:center;line-height:18px;border-radius:2px}
.bottom-bar{left:71px;top:1142px;width:629px;height:34px;background:var(--dark);display:flex;align-items:center;justify-content:space-between;padding:0 26px}
.copy{font-family:"Gelasio",serif;font-style:italic;font-size:7.5px;color:#aaa}
.bar-right{display:flex;align-items:center;gap:8px;font-family:"Gelasio",serif;font-size:10px;color:#aaa}
.social{width:16px;height:16px;border-radius:50%;background:#666}
</style>
</head>
<body>

<div class="abs brand"><span>maple lantern</span><span class="brand-dot"></span></div>
<nav class="abs nav">
  <a href="#">HOME</a><a href="#">ABOUT</a><a href="#">PORTFOLIO</a><a href="#">PRICING</a><a href="#">LOGIN</a><a class="current" href="#">CONTACT</a>
</nav>

<div class="abs top-rule"></div>
<div class="abs crumbs"><em>You are here:</em> Home » Contact</div>

<h1 class="abs page-title">Contact Us</h1>

<h2 class="abs label" style="left:97px;top:160px">BOOK A CONSULTATION</h2>
<p class="abs intro">Lorem ipsum dolor sit amet, consectetur adipisicing elit, sed do eiusmod tempor incididunt ut labore et dolore magna aliqua. Ut enim ad minim veniam, quis nostrud exercitation ullamco laboris nisi ut aliqu<br>ip ex ea commodo consequat. Duis aute irure dolor in reprehenderit in voluptate velit esse cillum dolore eu fugiat nulla pariatur. Excepteur sint occaecat cupidatat non proident, sunt in orem ipsum dolor sit amet, consectetur adipisicing elit, sed do eiusmod tempor incididunt ut labore et dolore magna aliqua. Ut enim ad minim veniam, quis nostrud exercitation ullamco laboris nisi ut aliqu</p>

<h2 class="abs label" style="left:545px;top:160px">CONTACT DETAILS</h2>
<address class="abs details">Phone: +61 3 6200 1480<br>Fax: +61 3 6200 1481<br>Email: info@maplelantern.com<br>L.N Some Streat Unknown<br>Location Of The Place<br>City - City Name<br>The Country</address>

<h2 class="abs label" style="left:97px;top:314px">ENTER YOUR QUERY</h2>
<div class="abs query-rule"></div>

<form class="abs form">
  <div class="field" style="top:28px">Name</div>
  <div class="field" style="top:62px">Email</div>
  <div class="field" style="top:95px">Telephone</div>
  <div class="field" style="top:128px;height:60px">Message</div>
  <div class="form-rule"></div>
  <div class="submit">Submit</div>
</form>

<h2 class="abs label" style="left:101px;top:646px">OUR LOCATION</h2>
<div class="abs map" role="img" aria-label="Map of the studio location on the coast, with national parks, lakes and highways"></div>

<div class="abs footer-rule"></div>
<footer class="abs footer">
  <div class="col" style="left:25px">
    <h4>SIMPLER THAN EVER</h4>
    <p>Lorem ipsum dolor sit amet, consectetur adipiscing elit. Nullam malesuada massa eget nisl rutrum ac hendrerit ante fermentum. Vestibulum ante ipsum primis in faucibus orci luctus et ultrices posuere cubilia Curae.</p>
  </div>
  <div class="col" style="left:174px">
    <h4>IMPRESSIVE PORTRAITS</h4>
    <p>Nullam malesuada massa eget nisl rutrum ac hendrerit ante fermentum. Vestibulum ante ipsum primis in faucibus orci luctus et ultrices posuere cubilia Curae. Lorem ipsum dolor sit amet, consectetur adipiscing.</p>
  </div>
  <div class="col" style="left:323px">
    <h4>FROM THE BLOG</h4>
    <p>Lorem ipsum dolor sit amet, consectetur adipiscing elit.</p>
    <p class="gap">Nullam malesuada massa eget nisl rutrum ac hendrerit ante.</p>
    <p class="gap">Vestibulum ante ipsum primis in faucibus orci.</p>
  </div>
  <div class="col" style="left:473px">
    <h4>CONTACT US</h4>
    <p class="dark">Phone: +61 3 6200 1480<br>Fax: +61 3 6200 1481<br>Email: info@maplelantern.com<br>L.N Some Streat Unknown<br>Location Of The Place<br>City - City Name<br>The Country</p>
  </div>
  <span class="more" style="left:25px">Learn More »</span>
  <span class="more" style="left:174px">See Portrait Gallery »</span>
  <span class="more" style="left:323px">View All »</span>
  <div class="touch">Get In Touch</div>
</footer>

<div class="abs bottom-bar">
  <span class="copy">© Copyright - maple lantern photography</span>
  <div class="bar-right"><span>maple lantern</span><span class="social"></span><span class="social"></span><span class="social"></span></div>
</div>

</body>
</html>
```